Corporate Business Cards

We need a new design for all of our business cards. They are boring and need some life.

Industry/Entity Type

Business

Requirements
Must have
• Corporate Logo of some type (See attached Pyramid)

Corporate Phrase "Accelerating Cashflow"

```html
<!DOCTYPE html>
<html lang="en">
<head>
<meta charset="utf-8">
<title>Ledgerwell Finance — Business Cards</title>
<link rel="stylesheet" href="https://fonts.googleapis.com/css2?family=Tinos:wght@400&family=Open+Sans:wght@400&display=swap">
<style>
  :root {
    --page-bg: #e9e7e3;
    --card-deep: #262b6e;
    --card-mid: #3a4185;
    --card-light: #5b63a3;
    --ink-light: #e6e7f0;
    --ink-soft: #c9cbe0;
    --rule: #d7d9ea;
    --shadow: rgba(20, 22, 50, 0.28);
  }
  * { box-sizing: border-box; margin: 0; padding: 0; }
  html, body {
    width: 1200px;
    height: 808px;
    overflow: hidden;
    background: var(--page-bg);
  }
  .sheet {
    position: relative;
    width: 1200px;
    height: 808px;
  }
  .card {
    position: absolute;
    top: 236px;
    width: 520px;
    height: 336px;
    background: linear-gradient(215deg, var(--card-light) 0%, var(--card-mid) 45%, var(--card-deep) 100%);
    box-shadow: 0 6px 18px var(--shadow);
    color: var(--ink-light);
    overflow: hidden;
  }
  .card--front { left: 50px; }
  .card--back { left: 630px; }

  .brand {
    display: flex;
    align-items: center;
    font-family: "Tinos", "Times New Roman", serif;
    font-weight: 400;
    color: var(--ink-light);
    text-transform: uppercase;
    line-height: 1;
  }
  .brand__mark {
    flex: none;
    background: var(--ink-soft);
  }
  .brand__name { display: flex; flex-direction: column; }

  .card--front .brand {
    position: absolute;
    left: 62px;
    top: 118px;
    gap: 22px;
  }
  .card--front .brand__mark { width: 66px; height: 66px; }
  .card--front .brand__name { font-size: 40px; gap: 6px; letter-spacing: 0.5px; }
  .card--front .brand__name span:last-child { padding-left: 4px; }

  .tagline {
    position: absolute;
    left: 150px;
    top: 216px;
    font-family: "Open Sans", Arial, sans-serif;
    font-size: 13px;
    letter-spacing: 3px;
    text-transform: uppercase;
    color: var(--ink-soft);
  }

  .card--back .brand {
    position: absolute;
    left: 34px;
    top: 34px;
    gap: 12px;
  }
  .card--back .brand__mark { width: 30px; height: 30px; }
  .card--back .brand__name { font-size: 17px; gap: 3px; }
  .card--back .brand__name span:last-child { padding-left: 2px; }

  .holder {
    position: absolute;
    left: 34px;
    top: 150px;
    width: 452px;
    font-family: "Open Sans", Arial, sans-serif;
  }
  .holder__name { font-size: 19px; color: var(--ink-light); }
  .holder__role { font-size: 13px; color: var(--ink-soft); margin-top: 2px; }
  .holder__rule {
    height: 1px;
    background: var(--rule);
    margin-top: 6px;
    margin-left: 78px;
  }

  .contact {
    position: absolute;
    top: 228px;
    font-family: "Open Sans", Arial, sans-serif;
    font-size: 12.5px;
    line-height: 1.6;
    color: var(--ink-soft);
    list-style: none;
  }
  .contact--left { left: 34px; }
  .contact--right { left: 286px; }

  .footer-rule {
    position: absolute;
    left: 286px;
    right: 34px;
    top: 290px;
    height: 1px;
    background: var(--rule);
  }
</style>
</head>
<body>
  <main class="sheet">
    <section class="card card--front" aria-label="Business card front">
      <div class="brand">
        <span class="brand__mark" aria-hidden="true"></span>
        <span class="brand__name"><span>Ledgerwell</span><span>Finance</span></span>
      </div>
      <p class="tagline">Accelerating Cashflow</p>
    </section>

    <section class="card card--back" aria-label="Business card back">
      <div class="brand">
        <span class="brand__mark" aria-hidden="true"></span>
        <span class="brand__name"><span>Ledgerwell</span><span>Finance</span></span>
      </div>

      <div class="holder">
        <p class="holder__name">Your name</p>
        <p class="holder__role">Position</p>
        <div class="holder__rule"></div>
      </div>

      <ul class="contact contact--left">
        <li>Address: xxxxxxxxxxx xxxx</li>
        <li>Phone: xxxxxxxxx xxxxxxx</li>
      </ul>
      <ul class="contact contact--right">
        <li>Email: xxxxxxxxxx xxxx</li>
        <li>Web: xxxxxxxx xxxxxxx</li>
      </ul>
      <div class="footer-rule"></div>
    </section>
  </main>
</body>
</html>
```